Business Card (I don't have a logo)

I'm bootstrapping a new venture and need a business card and "look" for it. I'd like to print one side only, but could do a bleed to the edges, but don't need to. See my website: www.calebharrowpartners.example to get a sense of the photos that relate to the look/feel of my company.

Target Market(s)

high tech start-up company CEO's in Silicon Valley

Industry/Entity Type

Business

Requirements
Must have
• a look that can cut/paste onto my website that integrates easily with the front page photo. see www.calebharrowpartners.example

```html
<!DOCTYPE html>
<html lang="en">
<head>
<meta charset="utf-8">
<title>Caleb Harrow — Business Card</title>
<link rel="stylesheet" href="https://fonts.googleapis.com/css2?family=Audiowide&display=swap">
<style>
  :root {
    --backdrop: #2a2c30;
    --card-deep: #1540b8;
    --card-mid: #2457d8;
    --card-light: #3a6cec;
    --ink-white: #f2f5ff;
    --ink-dark: #0a0f24;
    --ink-faint: rgba(205, 220, 255, 0.55);
  }
  * { box-sizing: border-box; margin: 0; padding: 0; }
  html, body {
    width: 1200px;
    height: 900px;
    overflow: hidden;
    background: var(--backdrop);
  }
  .canvas {
    width: 1200px;
    height: 900px;
    display: flex;
    align-items: center;
    justify-content: center;
  }
  .card {
    position: relative;
    width: 840px;
    height: 480px;
    border-radius: 36px;
    overflow: hidden;
    font-family: "Audiowide", "Arial Black", sans-serif;
    text-transform: uppercase;
    color: var(--ink-white);
    box-shadow: 0 20px 50px rgba(0, 0, 0, 0.45);
  }
  .card-texture {
    position: absolute;
    inset: 0;
    background:
      radial-gradient(ellipse at 30% 20%, rgba(255,255,255,0.10), transparent 60%),
      linear-gradient(160deg, var(--card-light) 0%, var(--card-mid) 45%, var(--card-deep) 100%);
  }
  .site-tag {
    position: absolute;
    top: 86px;
    right: 58px;
    font-size: 17px;
    letter-spacing: 1.5px;
    text-transform: lowercase;
    color: var(--ink-faint);
  }
  .contact {
    position: absolute;
    left: 52px;
    top: 212px;
    font-size: 17px;
    letter-spacing: 1.5px;
    line-height: 1.9;
  }
  .contact .name { color: var(--ink-dark); }
  .contact .label, .contact .at { color: var(--ink-dark); }
  .web-address {
    position: absolute;
    left: 52px;
    bottom: 70px;
    font-size: 26px;
    letter-spacing: 2.5px;
    white-space: nowrap;
  }
  .web-address .accent { color: var(--ink-dark); }
</style>
</head>
<body>
  <main class="canvas">
    <article class="card">
      <div class="card-texture" role="img" aria-label="Subtle woven diamond pattern across the blue card surface"></div>
      <p class="site-tag">calebharrowpartners.example</p>
      <div class="contact">
        <p class="name">Caleb Harrow</p>
        <p class="email"><span class="label">E |</span> caleb<span class="at">@</span>calebharrowpartners.example</p>
        <p class="phone"><span class="label">T |</span> 12345 555-0142</p>
      </div>
      <p class="web-address">www.caleb<span class="accent">harrow</span>partners.example</p>
    </article>
  </main>
</body>
</html>
```